Hurricane Damage Public Adjuster Billboard

I have created several projects with you and have several great designs. I need to format them into a Billboard for upcoming Hurricane Season. Need done in a month. Im also in process of getting an eye catching and easy to remember 800# Vanity phone number like Call 800-Stormfix or 800- Need Help? My included past Sketch Guild projects will give you an idea of what colors, schemes, and designs I gravitate towards. 3 past Design projects were 1) 2 Logos where I picked the 1st place and the 2nd place and 2) Index Card where I picked the winner as the Index Card and the 2nd place as a Post Card. Point is, I will pick and pay for 2 winners if they're good. This should help to sweeten the pot. Also, please look at my website for ideas that I like:

www.TheClaimWardenGroup.com
I want people to feel that I am the best and highest. Level.

I've been getting a lot of quick half effort designs basically cut & pasting my previous projects. Please don't rush and take your time to be creative. A an example, my Biggest Competitor is Crestline Public Adjusting. Their colors are Black and Gold while mine are Blue, White, and Black with a highlight of Orange if possible. I JUST imported a picture of their BillBoard. I need mine better and BLOW AWAY THEIRS. Terms like "Don't be Victimized Twice ?, Don't let the Hurricane Ruin your Life?". "Get Fairly Paid & Move On" "Our Clients Claims are VIP?
Updates

I'm getting a lot of quick half effort ones. I'd rather you take your time and really put some thoughts and effort into it. My Biggest Competitor is Crestline Public Adjusting. They have black & gold colors, while I have Blue, Black, and white.

It needs to blow theirs away. I have imported their Billboard for comparative purposes.

Guy's,
I'll make it easier for you in what I'm looking for. Please look at the Crestline Billboard picture attached.

1) Put my "Blue Shield" to the left, replacing their logo
2) change color patterns from their (Black, Gold, White) to my color schemes of (Black, Blue, White)
3) I want to see my name where their is:

THE
Claim Warden Group
EXPERT & LOCAL Public Adjusters
"FOR THE POLICYHOLDER!!"

4) to the right, add the A+Rated logo and QTR+ Accredited logo, 5 Star Zentrio Rated logo, 5 Start BLOCKLINK Highly Rated logo, etc..

5) the right side is where you can be creative as I will not have a picture of me there.

"20+ Years of Experience, Recovering Millions for our VIP Clients"

"Your Best, Locally-Based Private Adjuster & Advocate'
"FOR THE POLICYHOLDER!!"

"Don't be victimized Twice!!"

"Don't let the Hurricane Ruin Your Life!!"

This should really help. Also, refer to my website, maybe a couple testimonial fillers?

Thanks all,

marvin@TheClaimWardenGroup.com

Just imported a few awards that would look great to the right side with all the other 5 Star Ratings and accolades.
This right section could be titled like zmy Website:

5 Star Reviews, Ratings & Awards:
4-5 Logos underneath?

Target Market(s)

Coastal place where a Hurricane 🌀 🌀 Hits

Industry/Entity Type

Hurricane Public Insurance Adjuster

Font styles to use
Sans Serif
Other font styles liked:
• Calvera fonts

Colors
0054AA
0677BA
7BADD7
CADEEF
E8F1F8
EE7325
F08F49
F5BC92
FAE3D3
FDF4ED

Requirements
Must have
• Use my past project logos, colors, and schemes to create eye grabbing BillBoard
Nice to have
Should not have
• Not be too busy, must be Easy to Read, Eye Catchy

```html
<!DOCTYPE html>
<html lang="en">
<head>
<meta charset="utf-8">
<title>The Claim Warden Group – Hurricane Season Billboard</title>
<link rel="stylesheet" href="https://fonts.googleapis.com/css2?family=Anton&family=Oswald:wght@500;600;700&family=Montserrat:ital,wght@0,500;0,700;1,600&display=swap">
<style>
  :root {
    --ink: #141414;
    --blue-deep: #0054aa;
    --blue: #0677ba;
    --blue-bright: #1fa8e6;
    --blue-sky: #3fc2f2;
    --paper: #ffffff;
    --stage: #e8f1f8;
    --red: #e8262c;
    --green: #3fbf2a;
    --star: #f5a623;
    --zentrio: #3a6fd8;
    --seal: #1d4a73;
  }
  * { box-sizing: border-box; margin: 0; padding: 0; }
  html, body { width: 1200px; height: 971px; overflow: hidden; }
  body {
    background: var(--stage);
    display: flex; align-items: center; justify-content: center;
    font-family: "Montserrat", sans-serif;
  }
  .billboard {
    position: relative; width: 1120px; height: 474px;
    color: var(--paper);
    box-shadow: 0 18px 40px rgba(0, 40, 90, .25);
  }
  .billboard__art { position: absolute; inset: 0; }
  .headline {
    position: absolute; left: 70px; top: 30px; width: 600px;
    font-family: "Anton", sans-serif; font-size: 54px; line-height: 1.1;
    text-align: center; letter-spacing: .5px; white-space: nowrap;
  }
  .brand { position: absolute; left: 40px; top: 186px; width: 620px; height: 170px; }
  .brand__mark {
    position: absolute; left: 4px; top: 18px; width: 130px; height: 130px;
    border-radius: 50%; background: var(--blue-bright);
  }
  .brand__name {
    position: absolute; left: 160px; top: 20px;
    font-family: "Oswald", sans-serif; font-weight: 600; font-size: 42px; line-height: 1.1;
    color: var(--blue-sky); letter-spacing: 1px; white-space: nowrap;
  }
  .brand__role {
    position: absolute; left: 162px; top: 84px;
    font-family: "Montserrat", sans-serif; font-weight: 500; font-size: 19px;
    letter-spacing: 2.5px; white-space: nowrap;
  }
  .brand__tagline {
    position: absolute; left: 212px; top: 118px;
    font-family: "Montserrat", sans-serif; font-style: italic; font-weight: 600;
    font-size: 22px; color: var(--blue-sky); white-space: nowrap;
  }
  .pitch {
    position: absolute; left: 730px; top: 60px; width: 380px; text-align: center;
    font-family: "Oswald", sans-serif; font-weight: 700;
  }
  .pitch__title {
    font-family: "Anton", sans-serif; font-weight: 400;
    font-size: 31px; line-height: 1.1; letter-spacing: .3px; white-space: nowrap;
  }
  .pitch__rule { height: 1px; background: rgba(255,255,255,.85); margin: 14px 12px; }
  .pitch__claim { font-size: 25px; font-style: italic; line-height: 1.25; white-space: nowrap; }
  .pitch__proof { font-size: 16px; font-weight: 500; line-height: 1.4; margin-top: 18px; }
  .awards-title {
    position: absolute; left: 770px; top: 366px; width: 340px; text-align: center;
    font-family: "Oswald", sans-serif; font-weight: 500; font-size: 18px;
    letter-spacing: .3px; white-space: nowrap;
  }
  .cta {
    position: absolute; left: 26px; top: 392px; height: 76px;
    display: flex; align-items: center; gap: 22px;
  }
  .cta__label {
    font-family: "Oswald", sans-serif; font-weight: 700; font-size: 22px; line-height: 1.1;
    white-space: nowrap;
  }
  .cta__contact { display: flex; flex-direction: column; }
  .cta__phone {
    display: flex; align-items: center; gap: 10px;
    font-family: "Montserrat", sans-serif; font-weight: 700; font-size: 36px; line-height: 1;
    white-space: nowrap;
  }
  .cta__web {
    font-family: "Oswald", sans-serif; font-weight: 600; font-size: 16px;
    letter-spacing: 1.3px; margin-top: 6px; padding-left: 8px; white-space: nowrap;
  }
  .ratings {
    position: absolute; left: 580px; top: 402px; width: 540px; height: 72px;
    display: flex; align-items: center; justify-content: space-between;
    padding: 0 22px 0 70px; color: var(--ink);
  }
  .rating { white-space: nowrap; }
  .rating--grade { font-family: "Montserrat", sans-serif; font-weight: 700; font-size: 22px; color: var(--red); }
  .rating--badge { display: flex; flex-direction: column; align-items: center; gap: 3px; }
  .rating__seal { width: 84px; height: 36px; border-radius: 4px; background: var(--seal); }
  .rating__note { font-size: 8px; font-weight: 700; color: var(--seal); }
  .rating--zentrio { display: flex; flex-direction: column; align-items: center; gap: 2px; }
  .rating__name { font-family: "Montserrat", sans-serif; font-weight: 700; font-size: 22px; line-height: 1; }
  .rating--zentrio .rating__name { color: var(--zentrio); }
  .rating__stars { color: var(--star); font-size: 12px; letter-spacing: 1px; }
  .rating--blocklink .rating__name { color: var(--green); font-size: 19px; }
</style>
</head>
<body>
  <main class="billboard">
    <svg class="billboard__art" width="1120" height="474" viewBox="0 0 1120 474" aria-hidden="true">
      <defs>
        <linearGradient id="panelBlue" x1="0" y1="0" x2="1" y2="1">
          <stop offset="0" stop-color="#1fa8e6"/>
          <stop offset="1" stop-color="#0677ba"/>
        </linearGradient>
        <linearGradient id="bandBlue" x1="0" y1="0" x2="1" y2="0">
          <stop offset="0" stop-color="#0677ba"/>
          <stop offset="1" stop-color="#1fa8e6"/>
        </linearGradient>
      </defs>
      <rect width="1120" height="474" fill="#141414"/>
      <path d="M705 0 C690 150 710 300 790 402 L1120 402 L1120 0 Z" fill="url(#panelBlue)"/>
      <path d="M0 380 L470 380 Q505 380 525 400 L598 474 L0 474 Z" fill="url(#bandBlue)"/>
      <path d="M560 402 L1120 402 L1120 474 L612 474 Z" fill="#ffffff"/>
    </svg>

    <h1 class="headline">DON'T LET THE HURRICANE<br>RUIN YOUR LIFE!!</h1>

    <div class="brand">
      <span class="brand__mark"></span>
      <p class="brand__name">THE CLAIM WARDEN GROUP</p>
      <p class="brand__role">EXPERT &amp; LOCAL PUBLIC ADJUSTERS</p>
      <p class="brand__tagline">"FOR THE POLICYHOLDER!!"</p>
    </div>

    <section class="pitch">
      <h2 class="pitch__title">DON'T BE VICTIMIZED TWICE!</h2>
      <div class="pitch__rule"></div>
      <p class="pitch__claim">YOUR BEST, LOCALLY-BASED<br>PRIVATE ADJUSTER &amp; ADVOCATE!</p>
      <div class="pitch__rule"></div>
      <p class="pitch__proof">20+ YEARS OF EXPERIENCE, RECOVERING<br>MILLIONS FOR OUR VIP CLIENTS!</p>
    </section>

    <p class="awards-title">5 STAR REVIEWS, RATINGS &amp; AWARDS:</p>

    <div class="cta">
      <p class="cta__label">CALL US<br>TODAY!</p>
      <div class="cta__contact">
        <p class="cta__phone">
          <svg width="38" height="38" viewBox="0 0 40 40" aria-hidden="true">
            <circle cx="20" cy="20" r="19" fill="#ffffff"/>
            <path d="M14 10 L18 10 L19.5 15 L17 17 Q19 22 23 23.5 L25 21 L30 22.5 L30 26.5 Q29 29.5 25.5 29.5 Q11 27 10.5 13.5 Q10.5 10 14 10 Z" fill="#0677ba"/>
          </svg>
          (555) 204-7781
        </p>
        <p class="cta__web">WWW.THECLAIMWARDENGROUP.COM</p>
      </div>
    </div>

    <div class="ratings">
      <span class="rating rating--grade">A+ Rating</span>
      <span class="rating rating--badge">
        <span class="rating__seal"></span>
        <span class="rating__note">QTR Rating: A+</span>
      </span>
      <span class="rating rating--zentrio">
        <span class="rating__name">Zentrio</span>
        <span class="rating__stars">★★★★★</span>
      </span>
      <span class="rating rating--blocklink"><span class="rating__name">BLOCKLINK</span></span>
    </div>
  </main>
</body>
</html>
```